Bookcover: Ways to Turn Into a Bold Pathfinder

I am publishing a super-low-cost innovation book for €4,99 on Pageleaf Open Press to help everyone become a great innovator: young ambitious people without college education nor a big budget. Do you want to help me?

Brief:
Design a book cover 1600 x 2560 pixels for POP.
Main title: Ways to Turn Into a Bold Pathfinder
Sub title: mindset - insights - skills & tools
Author: Maarten de Kolkema
Design: captive, and appealing to everyone
Target Group: young ambitious people without college education

For pageleaf please format the height/width ratio of 1.6:1

```html
<!DOCTYPE html>
<html lang="en">
<head>
<meta charset="utf-8">
<title>Ways to Turn Into a Bold Pathfinder — Book Cover</title>
<link rel="stylesheet" href="https://fonts.googleapis.com/css2?family=Bebas+Neue&family=Poppins:wght@800&display=swap">
<style>
  :root {
    --page-white: #ffffff;
    --cover-blue: #034ea2;
    --accent-yellow: #f5d543;
    --title-white: #ffffff;
  }
  html, body {
    margin: 0;
    padding: 0;
    width: 1200px;
    height: 1200px;
    overflow: hidden;
    background: var(--page-white);
  }
  .canvas {
    position: relative;
    width: 1200px;
    height: 1200px;
    background: var(--page-white);
  }
  .book-cover {
    position: absolute;
    left: 295px;
    top: 141px;
    width: 618px;
    height: 925px;
    background: var(--cover-blue);
    overflow: hidden;
  }
  .cover-type {
    position: absolute;
    left: 0;
    top: 0;
    width: 618px;
    height: 845px;
    font-family: "Bebas Neue", "Arial Narrow", sans-serif;
  }
  .title-line { fill: var(--title-white); }
  .title-line--accent { fill: var(--accent-yellow); }
  .subtitle-line { fill: var(--title-white); }
  .bulb-artwork {
    position: absolute;
    left: 411px;
    top: 615px;
    width: 197px;
    height: 213px;
    border-radius: 50%;
    background: radial-gradient(circle at 50% 45%, var(--accent-yellow) 0%, rgba(245, 213, 67, 0.85) 40%, rgba(245, 213, 67, 0) 72%);
  }
  .author-band {
    position: absolute;
    left: 0;
    bottom: 0;
    width: 100%;
    height: 80px;
    background: var(--accent-yellow);
    display: flex;
    align-items: center;
    justify-content: center;
  }
  .author-name {
    margin: 0;
    font-family: "Poppins", "Helvetica Neue", Arial, sans-serif;
    font-weight: 800;
    font-size: 31px;
    letter-spacing: 0.5px;
    color: var(--cover-blue);
    text-transform: uppercase;
    line-height: 1;
  }
</style>
</head>
<body>
  <main class="canvas">
    <article class="book-cover">
      <svg class="cover-type" viewBox="0 0 618 845" xmlns="http://www.w3.org/2000/svg" aria-label="Ways to Turn Into a Bold Pathfinder. Mindset - insights - skills and tools">
        <text class="title-line" x="35" y="179" font-size="157" textLength="380" lengthAdjust="spacingAndGlyphs">WAYS TO</text>
        <text class="title-line" x="35" y="306" font-size="157" textLength="545" lengthAdjust="spacingAndGlyphs">TURN INTO A</text>
        <text class="title-line title-line--accent" x="35" y="473" font-size="209" textLength="310" lengthAdjust="spacingAndGlyphs">BOLD</text>
        <text class="title-line title-line--accent" x="35" y="609" font-size="168" textLength="548" lengthAdjust="spacingAndGlyphs">PATHFINDER</text>
        <text class="subtitle-line" x="41" y="690" font-size="58" textLength="359" lengthAdjust="spacingAndGlyphs">MINDSET - INSIGHTS -</text>
        <text class="subtitle-line" x="41" y="759" font-size="58" textLength="258" lengthAdjust="spacingAndGlyphs">SKILLS &amp; TOOLS</text>
      </svg>
      <div class="bulb-artwork" role="img" aria-label="Illustration of a glowing light bulb made of crumpled yellow paper with light rays"></div>
      <footer class="author-band">
        <p class="author-name">Maarten de Kolkema</p>
      </footer>
    </article>
  </main>
</body>
</html>
```